Business Card Design Project

use presentation folder design and my logo and make 4 over 4 business cards

Industry/Entity Type

Business

Requirements
Must have
• use the design from my presentation folder and put my logo on it

Name
Title
phone
fax
email

```html
<!DOCTYPE html>
<html lang="en">
<head>
<meta charset="utf-8">
<title>Harborline Counseling – Business Cards</title>
<link rel="stylesheet" href="https://fonts.googleapis.com/css2?family=Questrial&display=swap">
<style>
  :root {
    --page-bg: #e6e4e2;
    --front-taupe-dark: #a59d98;
    --front-taupe-light: #c9c6c4;
    --front-peach: #dec5b5;
    --back-peach: #f0dfd4;
    --back-peach-deep: #e2c5b3;
    --brand-brown: #a85a24;
    --ink: #2e2a28;
    --title-tan: #b38763;
    --label-brown: #8a4b1e;
  }
  * { margin: 0; padding: 0; box-sizing: border-box; }
  html, body {
    width: 1200px;
    height: 1000px;
    overflow: hidden;
    background: var(--page-bg);
    font-family: "Questrial", sans-serif;
  }
  .card {
    position: absolute;
    width: 640px;
    height: 366px;
    overflow: hidden;
    box-shadow: 0 6px 18px rgba(0,0,0,0.18);
  }
  .card-front {
    left: 70px;
    top: 100px;
    background: linear-gradient(120deg, var(--front-taupe-dark), var(--front-taupe-light));
  }
  .card-back {
    left: 490px;
    top: 540px;
    background: var(--back-peach);
  }
  .card-curve {
    position: absolute;
    inset: 0;
    width: 100%;
    height: 100%;
  }
  .brand {
    position: absolute;
    display: flex;
    flex-direction: column;
  }
  .brand-row {
    display: flex;
    align-items: center;
    gap: 10px;
  }
  .brand-dot {
    border-radius: 50%;
    background: var(--brand-brown);
  }
  .brand-name {
    color: var(--brand-brown);
    font-weight: 400;
  }
  .brand-tagline {
    color: var(--ink);
    letter-spacing: 0.5px;
  }
  .card-front .brand { left: 200px; top: 135px; }
  .card-front .brand-dot { width: 26px; height: 26px; }
  .card-front .brand-name { font-size: 28px; }
  .card-front .brand-tagline { font-size: 15px; margin-top: 6px; }

  .card-back .brand { right: 26px; top: 22px; align-items: flex-end; }
  .card-back .brand-dot { width: 16px; height: 16px; }
  .card-back .brand-name { font-size: 17px; }
  .card-back .brand-tagline { font-size: 10px; margin-top: 3px; }

  .person {
    position: absolute;
    left: 150px;
    top: 120px;
  }
  .person-name {
    font-size: 34px;
    color: var(--ink);
    letter-spacing: 1px;
  }
  .person-title {
    font-size: 19px;
    color: var(--title-tan);
    margin-left: 60px;
    letter-spacing: 0.5px;
  }
  .contact {
    position: absolute;
    left: 32px;
    bottom: 24px;
    list-style: none;
    font-size: 16px;
    line-height: 22px;
    color: var(--ink);
  }
  .contact-label {
    color: var(--label-brown);
    font-weight: 700;
    margin-right: 6px;
  }
</style>
</head>
<body>

  <section class="card card-front" aria-label="Card front">
    <svg class="card-curve" viewBox="0 0 640 366" preserveAspectRatio="none" aria-hidden="true">
      <path d="M640 0 C 560 40, 470 200, 420 366 L 640 366 Z" fill="var(--front-peach)"/>
    </svg>
    <div class="brand">
      <div class="brand-row">
        <span class="brand-dot"></span>
        <span class="brand-name">Harborline Counseling</span>
      </div>
      <span class="brand-tagline">a pro active addiction center</span>
    </div>
  </section>

  <section class="card card-back" aria-label="Card back">
    <svg class="card-curve" viewBox="0 0 640 366" preserveAspectRatio="none" aria-hidden="true">
      <path d="M330 0 C 430 30, 560 90, 640 150 L 640 0 Z" fill="var(--back-peach-deep)"/>
    </svg>
    <div class="brand">
      <div class="brand-row">
        <span class="brand-dot"></span>
        <span class="brand-name">Harborline Counseling</span>
      </div>
      <span class="brand-tagline">a pro active addiction center</span>
    </div>
    <div class="person">
      <p class="person-name">Elena Varga</p>
      <p class="person-title">markering manager</p>
    </div>
    <ul class="contact">
      <li><span class="contact-label">[P]</span>+11 555 0142</li>
      <li><span class="contact-label">[F]</span>+11 555 0198</li>
      <li><span class="contact-label">[E]</span>example@example.com</li>
    </ul>
  </section>

</body>
</html>
```